Interior Design & consultancy firm requires a new business card design that is a little bit funky bu

Kestrova Design Services is a leading strategic design practice specialising in the development and implementation of strategies and design solutions for commercial workplaces across a wide variety of industries.

The company has over twenty years experience in the strategic design, development and construction of innovative and efficient workplace environments for the commercial, corporate and industrial sectors.

We believe good design and efficient workspaces can transform companies, improve people’s lives and increase productivity.

Target Market(s)

My clients are mainly Government or corporate clients wanting to create a statement with their office fitout & new furniture that reflects their corporate identity

Industry/Entity Type

Construction

Font styles to use
Sans Serif

Colors
add136

Requirements
Must have
• The business card must be easy to read, simple & highlight my name & mobile phone number
Should not have
• I do not want the card to be fussy, feature too many colours or look to busy.

```html
<!DOCTYPE html>
<html lang="en">
<head>
<meta charset="utf-8">
<title>Kestrova Design Services – Business Card</title>
<link rel="stylesheet" href="https://fonts.googleapis.com/css2?family=Exo+2:wght@300;400;600&display=swap">
<style>
  :root {
    --brand-green: #add136;
    --brand-green-light: #d4ea5a;
    --brand-green-deep: #8cb51f;
    --paper-white: #ffffff;
    --paper-shade: #eceeea;
    --ink-grey: #555a55;
    --canvas-bg: #e7e6e2;
  }
  * { box-sizing: border-box; margin: 0; padding: 0; }
  html, body {
    width: 1200px;
    height: 1024px;
    overflow: hidden;
    background: var(--canvas-bg);
    font-family: "Exo 2", sans-serif;
  }
  .canvas {
    width: 1200px;
    height: 1024px;
    display: flex;
    flex-direction: column;
    align-items: center;
    justify-content: center;
    gap: 44px;
  }
  .card {
    position: relative;
    width: 800px;
    height: 457px;
    border-radius: 4px;
    overflow: hidden;
    box-shadow: 0 10px 30px rgba(0,0,0,0.15);
  }

  /* Front */
  .card-front {
    background: radial-gradient(ellipse at 62% 30%, var(--brand-green-light) 0%, var(--brand-green) 55%, var(--brand-green-deep) 100%);
  }
  .front-brand {
    position: absolute;
    left: 50%;
    top: 50%;
    transform: translate(-50%, -50%);
    display: flex;
    align-items: center;
    gap: 18px;
    color: var(--paper-white);
  }
  .brand-square {
    width: 46px;
    height: 46px;
    background: var(--paper-white);
    border-radius: 6px;
  }
  .brand-name {
    font-weight: 400;
    font-size: 30px;
    line-height: 1.15;
    letter-spacing: 0.5px;
  }

  /* Back */
  .card-back {
    background: linear-gradient(160deg, var(--paper-white) 0%, var(--paper-white) 55%, var(--paper-shade) 100%);
    border-bottom: 8px solid var(--brand-green);
  }
  .back-marker {
    position: absolute;
    left: 46px;
    top: 44px;
    width: 14px;
    height: 14px;
    background: var(--brand-green);
    border-radius: 2px;
  }
  .contact {
    position: absolute;
    left: 96px;
    top: 170px;
  }
  .contact-name {
    font-weight: 600;
    font-size: 30px;
    color: var(--brand-green-deep);
    letter-spacing: 0.3px;
  }
  .contact-title {
    margin-top: 6px;
    font-weight: 300;
    font-size: 18px;
    color: var(--ink-grey);
  }
  .contact-phone {
    margin-top: 26px;
    display: flex;
    align-items: center;
    gap: 10px;
    font-weight: 400;
    font-size: 22px;
    color: var(--ink-grey);
    letter-spacing: 1px;
  }
  .contact-phone svg { width: 18px; height: 18px; fill: var(--brand-green-deep); }
  .accent-blocks {
    position: absolute;
    right: 70px;
    bottom: 22px;
    display: flex;
    gap: 4px;
  }
  .accent-blocks span {
    display: block;
    width: 22px;
    height: 26px;
    background: var(--brand-green);
  }
  .accent-blocks span + span { opacity: 0.7; }
</style>
</head>
<body>
  <main class="canvas">
    <section class="card card-front" aria-label="Business card front">
      <div class="front-brand">
        <div class="brand-square"></div>
        <div class="brand-name">Kestrova<br>Design Services Pty Ltd</div>
      </div>
    </section>

    <section class="card card-back" aria-label="Business card back">
      <div class="back-marker"></div>
      <div class="contact">
        <p class="contact-name">Daniel Hartwell</p>
        <p class="contact-title">Interior Designer</p>
        <p class="contact-phone">
          <svg viewBox="0 0 24 24" aria-hidden="true"><path d="M6.6 10.8a15.1 15.1 0 0 0 6.6 6.6l2.2-2.2a1 1 0 0 1 1-.25 11.4 11.4 0 0 0 3.6.57 1 1 0 0 1 1 1V20a1 1 0 0 1-1 1A17 17 0 0 1 3 4a1 1 0 0 1 1-1h3.5a1 1 0 0 1 1 1c0 1.25.2 2.45.57 3.57a1 1 0 0 1-.25 1z"/></svg>
          04XXXXXXXX
        </p>
      </div>
      <div class="accent-blocks"><span></span><span></span></div>
    </section>
  </main>
</body>
</html>
```